Mobile Dental services for School Students

I need a double sided letter/flyer designed to go to principals of schools about our services.
I have attached an example of a previous flyer done and would like something similar except with our other company logo and stock photos etc.

Please have a look at the word doc as this is the layout I want and the information that needs to be included on the flyer.
The colour scheme is orange, green, white, grey etc. Basically the colours of the dental truck photo.

Please see attachments as all these need to be incorporated into the flyer.

Target Market(s)

Schools, Principals

Industry/Entity Type

School

Font styles to use
Serif
Sans Serif

Colors
f37122
00a990
959595
ffffff
606060

Requirements
Must have
• Email, phone number, website, logo etc.

```html
<!DOCTYPE html>
<html lang="en">
<head>
<meta charset="utf-8">
<title>BrightVan Dental – School Flyer</title>
<link href="https://fonts.googleapis.com/css2?family=Lato:wght@300;400;700;900&display=swap" rel="stylesheet">
<style>
:root{
  --orange:#f37122;
  --orange-soft:#f9c7a6;
  --teal:#00a990;
  --grey:#959595;
  --dark:#606060;
  --white:#ffffff;
  --stage:#e6e6e6;
}
*{box-sizing:border-box;margin:0;padding:0}
html,body{width:1200px;height:1200px;overflow:hidden}
body{background:var(--stage);font-family:'Lato',sans-serif;position:relative;color:var(--dark)}
.side-label{position:absolute;top:128px;font-size:48px;font-weight:400;color:var(--dark);font-family:'Lato',sans-serif}
.side-label.front{left:190px}
.side-label.back{left:870px}
.sheet{position:absolute;top:215px;width:662px;height:930px;background:var(--white);transform:scale(.8);transform-origin:0 0;overflow:hidden;box-shadow:0 4px 18px rgba(0,0,0,.18)}
.sheet.front{left:39px}
.sheet.back{left:628px}
.abs{position:absolute}

/* front */
.hero-photo{left:11px;top:11px;width:639px;height:238px;border-radius:40px 40px 0 40px;background:linear-gradient(100deg,#d9cfc6 0%,#5ec3c0 45%,#e8e3dd 70%,#2fb3a8 100%)}
.brand{left:0;width:100%;text-align:center;color:var(--teal);font-weight:900;line-height:1}
.front .brand{top:278px;font-size:46px}
.front .brand span{display:block;font-size:38px;margin-top:2px}
.quote-box{top:392px;width:290px;height:156px;border-radius:18px;border:4px solid var(--white);box-shadow:0 2px 8px rgba(0,0,0,.2);text-align:center;color:var(--white);display:flex;flex-direction:column;justify-content:center;align-items:center}
.quote-box.focus{left:28px;background:var(--teal)}
.quote-box.stat{left:341px;background:var(--orange);font-size:18px;font-weight:400;line-height:1.25;padding:0 14px}
.focus .lead{font-size:22px;font-weight:300}
.focus .big{font-size:27px;font-weight:700;margin-top:4px}
.focus .tag{font-size:26px;font-weight:700;background:var(--white);color:var(--teal);padding:0 10px;margin-top:4px;line-height:1.3}
.stat b{font-weight:700}
.qmark{width:38px;height:32px}
.intro-note{left:30px;width:602px;top:593px;font-size:11px;text-align:center;color:var(--dark);line-height:1.3}
.mascot{left:25px;top:640px;width:200px;height:260px;border-radius:50% 50% 20px 20px;background:linear-gradient(180deg,#f4f4f4,#d5d5d5)}
.book{left:240px;width:390px;top:668px;text-align:center;font-size:17px;line-height:1.3;color:var(--dark)}
.book b{font-weight:700}
.bright{left:240px;width:390px;top:726px;text-align:center;font-size:44px;font-weight:900;color:var(--teal)}
.bright .o{color:var(--orange)}
.bright .q{color:var(--dark);font-size:30px;vertical-align:super;font-weight:700}
.smile-art{left:340px;top:795px;width:170px;height:45px;border-radius:6px;background:linear-gradient(180deg,var(--white),var(--orange-soft))}
.footer-band{left:0;bottom:0;width:100%;height:72px}
.contacts{display:flex;gap:10px;color:var(--white);font-size:10px;align-items:center}
.contacts span{display:flex;align-items:center;gap:3px}
.contacts svg{width:9px;height:9px;fill:var(--white)}
.front .contacts{left:168px;top:886px}

/* back */
.truck-photo{left:0;top:0;width:662px;height:215px;background:linear-gradient(160deg,#f37122 0%,#00a990 35%,#dfe7e4 60%,#9aa3a0 100%)}
.back-swoosh{left:0;top:195px;width:662px;height:70px}
.letter{left:37px;width:603px;font-size:10px;line-height:1.3;color:var(--dark)}
.letter p{margin-bottom:6px}
.greeting{left:37px;top:268px;font-size:14px;font-weight:700;color:var(--dark)}
.offer-band{left:0;top:422px;width:100%;height:172px;background:var(--orange)}
.offer-pill{left:33px;top:411px;padding:3px 16px;background:var(--orange);border:3px solid var(--white);border-radius:20px;color:var(--white);font-size:20px;font-weight:700}
.offer-list{left:48px;top:460px;width:590px;color:var(--white);font-size:11px;line-height:1.3;list-style:none}
.offer-list li{position:relative;padding-left:16px;margin-bottom:8px}
.offer-list li::before{content:"";position:absolute;left:0;top:5px;width:4px;height:4px;border-radius:50%;background:var(--white)}
.call{left:35px;top:744px;font-size:15px;color:var(--dark)}
.call b{font-weight:700}
.call .num{color:var(--orange);font-weight:700}
.back .brand{left:52px;width:auto;top:790px;font-size:34px;text-align:left}
.back .brand span{display:block;font-size:28px;padding-left:70px}
.signoff{left:492px;top:787px;font-size:15px;font-weight:700;line-height:1.35;color:var(--dark)}
.back .contacts{left:105px;top:895px;gap:30px}
</style>
</head>
<body>
<div class="side-label front">front</div>
<div class="side-label back">back</div>

<section class="sheet front">
  <div class="abs hero-photo" role="img" aria-label="Photo of a smiling dental patient in the chair with a dentist and a smiling young man"></div>
  <div class="abs brand">BrightVan<span>Dental</span></div>

  <svg class="abs qmark" style="left:155px;top:372px" viewBox="0 0 38 32"><path fill="#00a990" d="M2 2h14v14l-6 14H4l5-12H2zM22 2h14v14l-6 14h-6l5-12h-7z"/></svg>
  <div class="abs quote-box focus">
    <div class="lead">Our focus is on</div>
    <div class="big">EDUCATION AND</div>
    <div class="tag">PREVENTION</div>
  </div>
  <svg class="abs qmark" style="left:160px;top:538px" viewBox="0 0 38 32"><path fill="#00a990" d="M2 2h14v14l-6 14H4l5-12H2zM22 2h14v14l-6 14h-6l5-12h-7z"/></svg>

  <svg class="abs qmark" style="left:467px;top:372px" viewBox="0 0 38 32"><path fill="#f37122" d="M2 2h14v14l-6 14H4l5-12H2zM22 2h14v14l-6 14h-6l5-12h-7z"/></svg>
  <div class="abs quote-box stat">
    <div><b>1 in 5 children</b> between the ages of <b>4-8 years of age</b> will suffer from tooth decay or dental caries as a result of poor dental hygiene</div>
  </div>
  <svg class="abs qmark" style="left:468px;top:538px;transform:rotate(180deg)" viewBox="0 0 38 32"><path fill="#f37122" d="M2 2h14v14l-6 14H4l5-12H2zM22 2h14v14l-6 14h-6l5-12h-7z"/></svg>

  <p class="abs intro-note">Thus, leading to possible dental destruction to their adult teeth. This, in conjunction with diet, lifestyle and social welfare can be contribution to the increase of child absenteeism.</p>

  <div class="abs mascot" role="img" aria-label="Tooth mascot character waving"></div>
  <p class="abs book">Book our services now for <b>2018</b> and help us,<br>Bring back your student’s</p>
  <div class="abs bright"><span class="q">“</span> BRIGHT <span class="o">SMILE</span> <span class="q">”</span></div>
  <div class="abs smile-art" role="img" aria-label="Orange smile graphic"></div>

  <svg class="abs footer-band" viewBox="0 0 662 72" preserveAspectRatio="none">
    <path d="M90 72 Q105 12 150 8 H662 V72Z" fill="#00a990"/>
    <path d="M72 72 Q90 18 140 14 H662 V72Z" fill="#f37122"/>
  </svg>
  <div class="abs contacts">
    <span><svg viewBox="0 0 10 10"><path d="M2 0l2 2-1 2 3 3 2-1 2 2-2 2C4 10 0 6 0 2z"/></svg>040 555 0182</span>
    <span><svg viewBox="0 0 10 10"><rect x="1" y="0" width="8" height="10" rx="1"/></svg>1800 555 019</span>
    <span><svg viewBox="0 0 10 10"><circle cx="5" cy="5" r="4.5"/></svg>www.brightvandental.com.au</span>
    <span><svg viewBox="0 0 10 10"><path d="M0 2h10v6H0z"/></svg>mara.k@brightvandental.com.au</span>
  </div>
</section>

<section class="sheet back">
  <div class="abs truck-photo" role="img" aria-label="Photo of the mobile dental clinic truck with branded orange and green livery"></div>
  <svg class="abs back-swoosh" viewBox="0 0 662 70" preserveAspectRatio="none">
    <path d="M0 0 H662 V20 H400 Q380 20 370 30 L350 70 H0Z" fill="#ffffff"/>
    <path d="M0 14 H330 Q355 14 362 35" fill="none" stroke="#f37122" stroke-width="6"/>
    <rect x="380" y="60" width="282" height="6" fill="#f37122"/>
  </svg>

  <div class="abs greeting">Dear Principal,</div>
  <div class="abs letter" style="top:291px">
    <p>We thank you for the time you are taking to review our mobile dental service. Here at BrightVan Dental, we are committed to ‘bring the dentist to you’.</p>
    <p>We are passionate about providing Bulked billed oral health care to all types of schools. We also service corporate companies, rural communities and aboriginal communities.</p>
    <p>Within Victoria, in the past year, we have serviced over 150 schools, and treated a total of 22,014 students so far.</p>
    <p>We are pleased to introduce our service designed to satisfy your student’s dental needs. Our service is cost effective, user friendly and extremely beneficial in providing oral health education and prevention.</p>
  </div>

  <div class="abs offer-band"></div>
  <div class="abs offer-pill">We offer</div>
  <ul class="abs offer-list">
    <li>Free Bulked Billed and treatment to students who qualify for the <b>“Child Dental Scheme”</b> program; this includes a dental check-up, cleaning &amp; fluoride treatments, sealants, x-rays and fillings.</li>
    <li>One-on-one oral health education from our professional dental clinicians.</li>
    <li>Complimentary Dental care pack comprising of a toothbrush, toothpaste and other products.</li>
    <li>Students also go into the draw to win various prices drawn after clinic’s visit to the school.</li>
    <li>Provide a referral to the student’s regular dentist for further treatment they may require.</li>
  </ul>

  <div class="abs letter" style="top:614px">
    <p>BrightVan Dental operates within accepted best practice models, and as such, is familiar, and without exception complies with the relevant legislation, regulations, codes and guidelines governing dentistry, including but not limited to, the dental code of conduct for Health Practitioners by the national dental board.</p>
    <p>Our mobile dental clinics feature state-of-the-art, oral health equipment and machinery. Including Digital x-rays systems that feature low dose radiation, as well as Approved Child Safety standard wheel chair access. All BrightVan Dental dentists, oral therapists and hygienists are licenses with the national dental board and have their working with children checks.</p>
    <p>Thank you for considering BrightVan Dental, my team and I look forward to providing this free service to your school and most importantly, ‘bringing the dentist to you’</p>
  </div>
  <p class="abs call">If you would like to book this service for <b>2018</b>, please give me a call on <span class="num">040 555 0182</span></p>

  <div class="abs brand">BrightVan<span>Dental</span></div>
  <div class="abs signoff">Kindest Regards,<br>Mara Kellan<br>Marketing Manager</div>

  <svg class="abs footer-band" viewBox="0 0 662 72" preserveAspectRatio="none">
    <path d="M62 72 Q72 14 120 12 H662 V72Z" fill="#f37122"/>
    <path d="M70 72 Q82 20 128 18 H662 V72Z" fill="#00a990"/>
  </svg>
  <div class="abs contacts">
    <span><svg viewBox="0 0 10 10"><path d="M2 0l2 2-1 2 3 3 2-1 2 2-2 2C4 10 0 6 0 2z"/></svg>040 555 0182</span>
    <span><svg viewBox="0 0 10 10"><rect x="1" y="0" width="8" height="10" rx="1"/></svg>1800 555 019</span>
    <span><svg viewBox="0 0 10 10"><circle cx="5" cy="5" r="4.5"/></svg>www.brightvandental.com.au</span>
    <span><svg viewBox="0 0 10 10"><path d="M0 2h10v6H0z"/></svg>mara.k@brightvandental.com.au</span>
  </div>
</section>
</body>
</html>
```